Real Estate Company Looking for Business Card Designs for 3 Executives

Hello!
Thanks so much for considering our project! We are a real estate investment company located in Edmonton, Alberta called Bellcrane Group of Companies. We invest/develop both commercial and residential real estate and are looking to create 3 DOUBLE-SIDED business cards for 3 top executives in the company! (for some reason it won't let us select the double-sided option, but yes, the cards are double sided and would be happy to tip extra)

We have certain guidelines that we want our business cards to for sure follow - the back of the Business card has to be the Black Background Version of the Logo which has already been designed and linked as a file (first file). We want the entire back of the card to simply just be the black background logo. In terms of the front of the card, would like to see a smaller version of the white background logo (linked as the second file) in the top left hand corner - of course, feel free to get creative and we can make revisions together along the way! and Then after that, just text. We want the card to be sharp, clean, easy on the eyes and highly professional looking. We would like the card to include the Full name of the Company (Bellcrane Group of Companies), Name of the Person, Title, Phone, Email. If possible please provide the front part of the card for 3 people:

1) Bellcrane Group of Companies, Nora Lindqvist, Chief Financial Officer, 780-555-0142, noralindqvist@bellcranegroup.example

2) Bellcrane Group of Companies, Julien Lindqvist, Chief Executive Officer, 780-555-0187, julienlindqvist@bellcranegroup.example

3) Bellcrane Group of Companies, Tom Okafor, Chief Operations Officer, 587-555-0163, tomokafor@bellcranegroup.example

Thank you so much for considering our project & we look forward to seeing your designs!

```html
<!DOCTYPE html>
<html lang="en">
<head>
<meta charset="utf-8">
<title>Bellcrane Business Card</title>
<link rel="stylesheet" href="https://fonts.googleapis.com/css2?family=Arimo:wght@400;700&display=swap">
<style>
  :root {
    --page-bg: #e6e6e5;
    --card-white: #ffffff;
    --card-dark: #2f2f2f;
    --ink: #2b2b2b;
    --ink-soft: #3a3a3a;
    --rule: #3a3a3a;
    --on-dark: #ffffff;
    --trunk-light: #7a7a7a;
    --trunk-dark: #1e1e1e;
  }
  * { box-sizing: border-box; margin: 0; padding: 0; }
  html, body {
    width: 1200px;
    height: 801px;
    overflow: hidden;
    background: var(--page-bg);
    font-family: "Arimo", Arial, sans-serif;
    color: var(--ink);
  }
  .sheet {
    position: relative;
    width: 1200px;
    height: 801px;
  }
  .card {
    position: absolute;
    top: 246px;
    width: 540px;
    height: 309px;
    overflow: hidden;
  }
  .card--front {
    left: 40px;
    background: var(--card-white);
  }
  .card--back {
    left: 620px;
    background: var(--card-dark);
  }

  /* Front */
  .front-wordmark {
    position: absolute;
    top: 70px;
    left: 300px;
    display: flex;
    align-items: center;
    gap: 10px;
    font-size: 17px;
    font-weight: 400;
    letter-spacing: 0.42em;
    color: var(--ink);
  }
  .wordmark-dot {
    width: 10px;
    height: 10px;
    background: var(--ink);
  }
  .person {
    position: absolute;
    left: 44px;
    top: 176px;
  }
  .person__name {
    font-size: 19px;
    font-weight: 700;
    letter-spacing: 0.01em;
    color: var(--ink);
  }
  .person__title {
    margin-top: 2px;
    font-size: 14.5px;
    font-weight: 400;
    color: var(--ink-soft);
  }
  .front-rule {
    position: absolute;
    left: 44px;
    right: 24px;
    top: 227px;
    height: 1.5px;
    background: var(--rule);
  }
  .contact {
    position: absolute;
    left: 44px;
    top: 238px;
    list-style: none;
    font-size: 14.5px;
    color: var(--ink-soft);
  }
  .contact__item {
    display: flex;
    align-items: center;
    gap: 10px;
    height: 21px;
  }
  .contact__icon {
    width: 12px;
    height: 12px;
    flex: none;
  }

  /* Back */
  .forest-art {
    position: absolute;
    left: 0;
    top: 0;
    width: 260px;
    height: 309px;
    background: linear-gradient(100deg, var(--trunk-dark) 0%, var(--card-dark) 30%, var(--trunk-light) 55%, var(--card-dark) 85%);
    opacity: 0.85;
  }
  .back-wordmark {
    position: absolute;
    top: 140px;
    left: 280px;
    display: flex;
    align-items: center;
    gap: 12px;
    font-size: 21px;
    font-weight: 400;
    letter-spacing: 0.42em;
    color: var(--on-dark);
  }
  .back-wordmark .wordmark-dot {
    width: 12px;
    height: 12px;
    background: var(--on-dark);
  }
</style>
</head>
<body>
<main class="sheet">
  <section class="card card--front" aria-label="Card front">
    <div class="front-wordmark"><span class="wordmark-dot"></span>BELLCRANE</div>

    <div class="person">
      <p class="person__name">NORA LINDQVIST</p>
      <p class="person__title">Chief Financial</p>
    </div>

    <div class="front-rule"></div>

    <ul class="contact">
      <li class="contact__item">
        <svg class="contact__icon" viewBox="0 0 12 12" aria-hidden="true">
          <path d="M2.5 1 L4.3 1 L5 3.2 L3.9 4.2 C4.5 5.6 5.9 7.1 7.6 7.9 L8.6 6.8 L11 7.5 L11 9.4 C11 10.2 10.3 10.8 9.5 10.7 C5 10.2 1.6 6.8 1.2 2.4 C1.1 1.6 1.7 1 2.5 1 Z" fill="#2b2b2b"/>
        </svg>
        <span>780-555-0142</span>
      </li>
      <li class="contact__item">
        <svg class="contact__icon" viewBox="0 0 12 12" aria-hidden="true">
          <rect x="0.7" y="2.2" width="10.6" height="7.6" fill="none" stroke="#2b2b2b" stroke-width="1.1"/>
          <path d="M0.9 2.5 L6 6.6 L11.1 2.5" fill="none" stroke="#2b2b2b" stroke-width="1.1"/>
        </svg>
        <span>noralindqvist@bellcranegroup.example</span>
      </li>
    </ul>
  </section>

  <section class="card card--back" aria-label="Card back">
    <div class="forest-art" role="img" aria-label="Tall tree trunks illustration in soft greys"></div>
    <div class="back-wordmark"><span class="wordmark-dot"></span>BELLCRANE</div>
  </section>
</main>
</body>
</html>
```